Workvine banner ad for roofing company

We need an ad created for a Workvine banner advertising campaign for a UK based roofing company.

The design should have a large photograph on the background (see attached).
The design should have our Ratewell rating (5 stars).
There should be a large text header at the top which reads "Your local roofing experts"

The following services should be listed:
- New roofs
- General roof repairs
- Drone surveys
- Single ply roofing
- Steel cladding
- Asbestos removal

The company logo needs to be visible (attached). Also the company telephone number 020 7946 0321 and website www.brantleyroofing.com

The advert needs to be horizontal/landscape design. For full spec, please see here: https://business.workvine-example.com/marketing-solutions/success/ads-guide/single-image-ads

Size required: 1.91:1 - 1200 x 628 pixels

```html
<!DOCTYPE html>
<html lang="en">
<head>
<meta charset="utf-8">
<title>Brantley Roofing – Your local roofing experts</title>
<link href="https://fonts.googleapis.com/css2?family=Rubik:wght@500;600&family=Roboto:wght@500;700&display=swap" rel="stylesheet">
<style>
  :root {
    --navy: #2c376b;
    --sky: #4ba6dd;
    --white: #ffffff;
    --photo-a: #5f8f9a;
    --photo-b: #3f7386;
    --photo-c: #7d9b80;
    --star: #4ba6dd;
  }
  * { box-sizing: border-box; margin: 0; padding: 0; }
  html, body { width: 1200px; height: 628px; overflow: hidden; background: var(--white); }
  .banner {
    position: relative; width: 1200px; height: 628px; overflow: hidden;
    font-family: "Roboto", Arial, sans-serif; color: var(--white);
  }
  .backdrop { position: absolute; inset: 0; }
  .brand {
    position: absolute; left: 100px; top: 38px;
    display: flex; align-items: center; gap: 10px;
  }
  .brand-dot {
    width: 38px; height: 38px; border-radius: 50%;
    border: 3px solid var(--white);
  }
  .brand-name {
    font-family: "Rubik", Arial, sans-serif; font-weight: 600;
    font-size: 29px; letter-spacing: -0.5px; color: var(--white);
  }
  .rating { position: absolute; left: 426px; top: 38px; }
  .rating-name {
    font-family: "Rubik", Arial, sans-serif; font-weight: 500; font-size: 16px;
    display: block; margin-bottom: 4px;
  }
  .rating-stars { display: flex; gap: 2px; }
  .headline {
    position: absolute; left: 100px; top: 128px;
    font-family: "Rubik", Arial, sans-serif; font-weight: 600;
    font-size: 45px; line-height: 54px; letter-spacing: -0.3px;
  }
  .headline .accent { color: var(--sky); display: block; }
  .services {
    position: absolute; left: 70px; top: 273px;
    display: grid; grid-template-columns: 174px 174px 174px;
    row-gap: 25px; list-style: none;
  }
  .service { display: flex; flex-direction: column; align-items: center; }
  .service-icon { width: 68px; height: 68px; }
  .service-label {
    margin-top: 15px; font-weight: 700; font-size: 14.5px; line-height: 17px;
    text-transform: uppercase; white-space: nowrap;
  }
  .contact {
    position: absolute; left: 100px; top: 564px;
    display: flex; align-items: center; font-weight: 500; font-size: 18px;
  }
  .contact-item { display: flex; align-items: center; gap: 23px; margin-right: 30px; }
  .contact-icon { width: 48px; height: 48px; }
  .contact-web { text-decoration: underline; text-underline-offset: 3px; font-size: 17px; }
</style>
</head>
<body>
<main class="banner">
  <svg class="backdrop" width="1200" height="628" viewBox="0 0 1200 628">
    <defs>
      <linearGradient id="photoWide" x1="0" y1="0" x2="1" y2="1">
        <stop offset="0" stop-color="var(--photo-a)"/>
        <stop offset="1" stop-color="var(--photo-b)"/>
      </linearGradient>
      <radialGradient id="photoRound" cx="0.5" cy="0.45" r="0.6">
        <stop offset="0" stop-color="#9aa39a"/>
        <stop offset="0.6" stop-color="var(--photo-c)"/>
        <stop offset="1" stop-color="#5a7c5c"/>
      </radialGradient>
      <clipPath id="roundClip"><circle cx="843" cy="311" r="222"/></clipPath>
    </defs>
    <rect width="1200" height="628" fill="url(#photoWide)" role="img" aria-label="Blue-tinted aerial photograph of residential blocks with flat roofs"/>
    <polygon points="0,0 530,0 860,330 650,628 0,628" fill="var(--navy)"/>
    <polyline points="530,0 860,330 650,628" fill="none" stroke="var(--white)" stroke-width="4"/>
    <circle cx="843" cy="311" r="240" fill="none" stroke="var(--white)" stroke-width="2.5"/>
    <circle cx="843" cy="311" r="224" fill="var(--white)"/>
    <rect x="618" y="86" width="450" height="450" fill="url(#photoRound)" clip-path="url(#roundClip)" role="img" aria-label="Drone photograph of flat-roofed apartment blocks surrounded by greenery and parking"/>
  </svg>

  <div class="brand">
    <span class="brand-dot"></span>
    <span class="brand-name">brantleyroofing</span>
  </div>

  <div class="rating">
    <span class="rating-name">Ratewell</span>
    <div class="rating-stars" aria-label="5 star rating">
      <svg width="92" height="18" viewBox="0 0 92 18">
        <g fill="var(--star)">
          <path id="star" d="M9 1l2.4 5.2 5.6.6-4.2 3.8 1.2 5.6L9 13.3 4 16.2l1.2-5.6L1 6.8l5.6-.6z"/>
          <use href="#star" x="18.5"/><use href="#star" x="37"/><use href="#star" x="55.5"/><use href="#star" x="74"/>
        </g>
      </svg>
    </div>
  </div>

  <h1 class="headline">Your local<span class="accent">roofing experts</span></h1>

  <ul class="services">
    <li class="service">
      <svg class="service-icon" viewBox="0 0 68 68"><circle cx="34" cy="34" r="32" fill="var(--white)"/><circle cx="34" cy="34" r="28" fill="none" stroke="var(--navy)" stroke-width="1.5"/><path d="M20 44l8-14h12l8 14z" fill="none" stroke="var(--sky)" stroke-width="2.5"/><rect x="30" y="22" width="6" height="8" fill="var(--navy)"/></svg>
      <span class="service-label">New roofs</span>
    </li>
    <li class="service">
      <svg class="service-icon" viewBox="0 0 68 68"><circle cx="34" cy="34" r="32" fill="var(--white)"/><circle cx="34" cy="34" r="28" fill="none" stroke="var(--navy)" stroke-width="1.5"/><path d="M20 44l14-12 14 12" fill="none" stroke="var(--navy)" stroke-width="2.5"/><path d="M26 22l14 14" stroke="var(--navy)" stroke-width="3"/><circle cx="36" cy="40" r="5" fill="none" stroke="var(--sky)" stroke-width="2"/></svg>
      <span class="service-label">General roof repairs</span>
    </li>
    <li class="service">
      <svg class="service-icon" viewBox="0 0 68 68"><circle cx="34" cy="34" r="32" fill="var(--white)"/><circle cx="34" cy="34" r="28" fill="none" stroke="var(--navy)" stroke-width="1.5"/><rect x="28" y="30" width="12" height="7" rx="2" fill="var(--navy)"/><path d="M18 28h10M40 28h10M22 28v4M46 28v4" stroke="var(--navy)" stroke-width="2"/><circle cx="34" cy="41" r="2.5" fill="var(--sky)"/></svg>
      <span class="service-label">Drone surveys</span>
    </li>
    <li class="service">
      <svg class="service-icon" viewBox="0 0 68 68"><circle cx="34" cy="34" r="32" fill="var(--white)"/><circle cx="34" cy="34" r="28" fill="none" stroke="var(--navy)" stroke-width="1.5"/><path d="M22 24l22-2 2 22-22 2z" fill="var(--sky)"/><circle cx="27" cy="28" r="1.8" fill="var(--white)"/><circle cx="40" cy="27" r="1.8" fill="var(--white)"/><circle cx="28" cy="41" r="1.8" fill="var(--white)"/><circle cx="41" cy="40" r="1.8" fill="var(--white)"/></svg>
      <span class="service-label">Steel cladding</span>
    </li>
    <li class="service">
      <svg class="service-icon" viewBox="0 0 68 68"><circle cx="34" cy="34" r="32" fill="var(--white)"/><circle cx="34" cy="34" r="28" fill="none" stroke="var(--navy)" stroke-width="1.5"/><path d="M18 42l16-16 16 16z" fill="var(--sky)"/><path d="M18 42l16-16 16 16" fill="none" stroke="var(--navy)" stroke-width="2.5"/></svg>
      <span class="service-label">Single ply roofing</span>
    </li>
    <li class="service">
      <svg class="service-icon" viewBox="0 0 68 68"><circle cx="34" cy="34" r="32" fill="var(--white)"/><circle cx="34" cy="34" r="28" fill="none" stroke="var(--navy)" stroke-width="1.5"/><g fill="var(--sky)"><rect x="21" y="22" width="5" height="24"/><rect x="29" y="22" width="5" height="24"/><rect x="37" y="22" width="5" height="24"/><rect x="45" y="22" width="3" height="24"/></g><path d="M20 30h28M20 38h28" stroke="var(--navy)" stroke-width="2"/></svg>
      <span class="service-label">Asbestos removal</span>
    </li>
  </ul>

  <div class="contact">
    <div class="contact-item">
      <svg class="contact-icon" viewBox="0 0 48 48"><circle cx="24" cy="24" r="24" fill="var(--sky)"/><path d="M18 15c1.5-1 3-.5 3.5.5l1.5 3.5c.4 1-.2 1.8-1 2.4l-1 .8c1 2.3 2.8 4.2 5 5.3l.9-1c.7-.8 1.5-1.2 2.5-.8l3.4 1.5c1 .5 1.4 2 .5 3.4-1.3 2-3.5 2.6-5.8 1.6-5-2.2-8.5-5.8-10.5-10.8-.8-2.2-.5-4.8 1-6.4z" fill="var(--white)"/></svg>
      <span>020 7946 0321</span>
    </div>
    <div class="contact-item">
      <svg class="contact-icon" viewBox="0 0 48 48"><circle cx="24" cy="24" r="24" fill="var(--sky)"/><circle cx="24" cy="24" r="9" fill="none" stroke="var(--white)" stroke-width="2"/><path d="M15 24h18M24 15c-4 5-4 13 0 18M24 15c4 5 4 13 0 18" fill="none" stroke="var(--white)" stroke-width="1.6"/></svg>
      <span class="contact-web">www.brantleyroofing.com</span>
    </div>
  </div>
</main>
</body>
</html>
```